Professional Business Cards

We need a nice looking, profession and modern business card for our new company. Our logo is attatched

Target Market(s)

Young Professionals

Industry/Entity Type

Financial

Contact Information for Business Card

FRONT

Morvane Tally Pty Ltd
Level 22, Halden Court, 48 Wirrapool St
Sydney NSW 2000
ABN : 57 304 918 226

Derek Wallis - Chief Operations Officer
P : 02 7153 2819
M: 0418 395 207
derek@morvanetally,com

BACK

- Cryptocurrency Exchange Services
- Cryptocurrency Mining Operations
- Cryptocurrency Investment Fund Offering

Font styles to use
Sans Serif

Colors
0255a3
9d9d9d

```html
<!DOCTYPE html>
<html lang="en">
<head>
<meta charset="utf-8">
<title>Morvane Tally – Business Card</title>
<link href="https://fonts.googleapis.com/css2?family=Michroma&family=Lato:wght@400;700&display=swap" rel="stylesheet">
<style>
  :root {
    --backdrop: #323232;
    --backdrop-top: #2d2d2d;
    --card-light: #ffffff;
    --card-dark: #03151d;
    --brand-blue: #0255a3;
    --brand-grey: #9d9d9d;
    --ink: #2b2b2b;
    --ink-light: #ffffff;
  }
  * { margin: 0; padding: 0; box-sizing: border-box; }
  html, body { width: 1200px; height: 900px; overflow: hidden; }
  body {
    background: radial-gradient(ellipse at 50% 40%, var(--backdrop) 0%, var(--backdrop-top) 100%);
    font-family: "Lato", sans-serif;
    position: relative;
  }
  .card {
    position: absolute;
    top: 306px;
    width: 440px;
    height: 271px;
    border-radius: 12px;
  }
  .card--front { left: 149px; background: var(--card-light); }
  .card--back { left: 608px; background: var(--card-dark); }

  /* front */
  .front-mark {
    position: absolute;
    left: 30px;
    top: 104px;
    display: flex;
    align-items: center;
    gap: 8px;
  }
  .mark-square {
    width: 16px; height: 16px;
    background: var(--brand-blue);
  }
  .front-mark .mark-name {
    font-family: "Lato", sans-serif;
    font-weight: 700;
    font-size: 17px;
    color: var(--brand-grey);
    letter-spacing: 0.3px;
  }
  .divider {
    position: absolute;
    left: 212px; top: 61px;
    width: 1px; height: 150px;
    background: var(--brand-blue);
  }
  .contact {
    position: absolute;
    left: 238px; top: 57px;
    color: var(--ink);
    font-size: 12.3px;
    line-height: 16px;
  }
  .contact__name {
    font-family: "Michroma", sans-serif;
    font-size: 13.5px;
    color: var(--brand-blue);
    line-height: 18px;
    letter-spacing: 0.3px;
  }
  .contact__role { margin-bottom: 4px; }
  .contact__lines { margin-top: 6px; list-style: none; }
  .contact__lines li { display: flex; align-items: center; gap: 5px; }
  .contact__lines svg { width: 10px; height: 10px; fill: var(--brand-blue); }
  .abn {
    position: absolute;
    left: 0; right: 0; top: 226px;
    text-align: center;
    font-size: 12.3px;
    color: var(--ink);
  }
  .abn__label { color: var(--brand-blue); }

  /* back */
  .back-mark {
    position: absolute;
    left: 0; right: 0; top: 105px;
    display: flex;
    justify-content: center;
    align-items: center;
    gap: 14px;
  }
  .back-mark .mark-square { width: 26px; height: 26px; }
  .back-mark .mark-name {
    font-family: "Lato", sans-serif;
    font-weight: 700;
    font-size: 38px;
    color: var(--brand-blue);
    letter-spacing: 1px;
    text-transform: uppercase;
    line-height: 1;
  }
  .services {
    position: absolute;
    left: 0; right: 0; top: 197px;
    list-style: none;
    text-align: center;
    color: var(--ink-light);
    font-size: 12.5px;
    line-height: 16px;
  }
</style>
</head>
<body>
  <section class="card card--front">
    <div class="front-mark">
      <span class="mark-square"></span>
      <span class="mark-name">Morvane Tally</span>
    </div>
    <span class="divider"></span>
    <div class="contact">
      <p class="contact__name">DEREK WALLIS</p>
      <p class="contact__role">Chief Operations Officer</p>
      <p>Morvane Tally Pty Ltd</p>
      <p>Level 22, Halden Court,</p>
      <p>48 Wirrapool St</p>
      <p>Sydney NSW 2000</p>
      <ul class="contact__lines">
        <li><svg viewBox="0 0 10 10"><path d="M1 3.5 C1 2 2.5 1.5 5 1.5 S9 2 9 3.5 L7 4.2 L6.5 3 L3.5 3 L3 4.2 Z M2.5 5 H7.5 L8.5 8.5 H1.5 Z"/></svg>02 7153 2819</li>
        <li><svg viewBox="0 0 10 10"><path d="M3 0.5 H7 A1 1 0 0 1 8 1.5 V8.5 A1 1 0 0 1 7 9.5 H3 A1 1 0 0 1 2 8.5 V1.5 A1 1 0 0 1 3 0.5 Z M3 2 V7.5 H7 V2 Z"/></svg>0418 395 207</li>
        <li><svg viewBox="0 0 10 10"><circle cx="5" cy="5" r="4.5"/><path d="M3 3.5 L5 3 L6 4.5 L4.5 6 L5 8 L3.5 7 Z" fill="#fff"/></svg>www.derek@morvanetally.com</li>
      </ul>
    </div>
    <p class="abn"><span class="abn__label">ABN</span> : 57 304 918 226</p>
  </section>

  <section class="card card--back">
    <div class="back-mark">
      <span class="mark-square"></span>
      <span class="mark-name">Morvane Tally</span>
    </div>
    <ul class="services">
      <li>Cryptocurrency Exchange Services</li>
      <li>Cryptocurrency Mining Operations</li>
      <li>Cryptocurrency Investment Fund Offering</li>
    </ul>
  </section>
</body>
</html>
```